Shopify Design for a Homeopathic Shop

The design should let the user give a feeling of luxury and naturality(earthy).

We want to build up a alternative medicine luxury brand. The user should have a feeling of trust when visiting our shop. We stand for natural remedies.

Target Market(s)

Alternative / Left

Industry/Entity Type

Alternative Medicine

Font styles to use
Sans Serif

Colors

Designer to choose colors to be used in the design.

```html
<!DOCTYPE html>
<html lang="en">
<head>
<meta charset="utf-8">
<title>Verdalis — Homeopathic Remedies</title>
<link href="https://fonts.googleapis.com/css2?family=Lato:wght@400;700&family=Open+Sans:wght@300;400;600;700&display=swap" rel="stylesheet">
<style>
:root{
  --green-dark:#167233;
  --green-nav:#1a7a36;
  --green-light:#7cc242;
  --ink:#333;
  --muted:#666;
  --price:#c8282e;
  --line:#dcdcdc;
  --topbar:#2a2a2a;
  --footer:#222;
  --white:#fff;
}
*{box-sizing:border-box;margin:0;padding:0}
html,body{width:1200px;height:3386px;overflow:hidden}
body{position:relative;font-family:"Lato",sans-serif;color:var(--ink);background:var(--white);font-size:14px}
.abs{position:absolute}
svg{display:block}
.btn{position:absolute;background:var(--green-light);color:var(--white);display:flex;align-items:center;justify-content:center;font-size:14px}

/* top bar */
.topbar{left:0;top:0;width:1200px;height:34px;background:var(--topbar);color:#eee;font-size:12px}
.topbar .item{position:absolute;top:0;height:34px;display:flex;align-items:center;gap:6px}
/* header */
.brand{position:absolute;display:flex;align-items:center;gap:8px;color:var(--green-dark);font-family:"Open Sans",sans-serif}
.brand .mark{width:14px;height:14px;border-radius:50%;background:var(--green-light)}
.brand .name{font-size:26px;letter-spacing:2px;font-weight:400}
.brand .tag{font-size:7px;letter-spacing:3px;position:absolute;left:22px;top:33px}
.select{left:375px;top:49px;width:157px;height:29px;background:var(--green-dark);color:#fff;font-size:13px;display:flex;align-items:center;padding-left:11px}
.select .chev{position:absolute;right:8px;top:7px;width:15px;height:15px;border-radius:50%;background:#e8e8e8}
.search{left:544px;top:49px;width:330px;height:29px;background:#f1f1f1;font-size:11px;color:#777;display:flex;align-items:center;padding-left:12px}
.nav{left:0;top:103px;width:1200px;height:46px;background:var(--green-nav);display:flex;align-items:center}
.nav a{position:absolute;top:0;height:46px;display:flex;align-items:center;justify-content:center;color:#fff;text-decoration:none;font-size:14px}
.nav .sep{position:absolute;top:13px;width:1px;height:20px;background:rgba(255,255,255,.25)}
/* hero */
.hero{left:0;top:149px;width:1200px;height:458px;background:linear-gradient(90deg,#6b4a30 0%,#8b6a4c 35%,#c9c2b4 60%,#e6e2da 78%,#7b5d40 100%)}
.hero h1{position:absolute;left:84px;top:152px;font-family:"Open Sans",sans-serif;font-weight:700;font-size:34px;color:#fff}
.hero p{position:absolute;left:83px;top:205px;width:360px;color:#fff;font-size:13.5px;line-height:17px}
.hero .arrow{position:absolute;top:210px}
.dots{position:absolute;left:566px;top:418px;display:flex;gap:9px}
.dots i{width:10px;height:10px;border-radius:50%;background:#fff}
.dots i:first-child{background:var(--green-light)}
/* features */
.feature{position:absolute;top:662px;display:flex;align-items:center;gap:14px}
.feature .t{font-family:"Open Sans",sans-serif;font-weight:700;font-size:14px;color:#333}
.feature .s{font-size:13px;color:#333}
.fsep{position:absolute;top:660px;width:2px;height:58px;background:#eee}
.sec-title{position:absolute;left:0;width:1200px;text-align:center;font-family:"Open Sans",sans-serif;font-weight:400;font-size:37px;color:#222;letter-spacing:.5px}
/* products */
.product{position:absolute;top:850px;width:237px}
.product .img{height:249px;border:1px solid var(--line);padding:12px}
.product .img div{width:100%;height:100%;background:radial-gradient(circle,#b9342c 0%,#6a2a1a 35%,#fff 70%)}
.product .nm{text-align:center;margin-top:20px;font-family:"Open Sans",sans-serif;font-size:14px;letter-spacing:1.5px;color:#333}
.product .pr{text-align:center;margin-top:6px;font-size:20px;letter-spacing:1.5px;color:var(--price)}
/* about */
.about-photo{left:0;top:1338px;width:601px;height:552px;background:linear-gradient(135deg,#6a5a2c 0%,#8e8a6a 35%,#d8d4c8 60%,#5d4530 100%)}
.about{left:601px;top:1338px;width:599px;height:552px;background:var(--green-dark);color:#fff}
.about h2{position:absolute;left:54px;top:68px;font-family:"Open Sans",sans-serif;font-weight:400;font-size:38px}
.about p{position:absolute;left:54px;width:480px;font-size:13.5px;line-height:16.5px}
/* blogs */
.blog{position:absolute;top:2006px;width:336px;height:389px;border:1px solid var(--line)}
.blog .img{position:absolute;left:12px;top:11px;width:312px;height:209px}
.blog .meta{position:absolute;left:18px;top:232px;right:18px;font-size:12px;color:#555;display:flex;align-items:center;gap:6px}
.blog .meta .r{margin-left:auto;display:flex;gap:18px}
.blog h3{position:absolute;left:18px;top:266px;font-family:"Open Sans",sans-serif;font-weight:400;font-size:14px;color:#333}
.blog p{position:absolute;left:18px;top:289px;width:300px;font-size:13px;line-height:16px;color:#555}
.blog .more{position:absolute;left:20px;top:354px;font-size:12px;color:#444;display:flex;align-items:center;gap:6px}
/* lists */
.list h4{position:absolute;top:2524px;font-family:"Open Sans",sans-serif;font-weight:400;font-size:28px;color:#222}
.row{position:absolute;display:flex;gap:13px}
.row .th{width:66px;height:64px;border:1px solid var(--line);display:flex;align-items:center;justify-content:center}
.row .th i{width:18px;height:44px;background:linear-gradient(#ddd 0 20%,#7a3a1a 20% 100%);border-radius:3px}
.row .nm{font-family:"Open Sans",sans-serif;font-size:14px;color:#333;letter-spacing:.5px;margin-top:3px}
.row .pr{font-size:14px;margin-top:6px;letter-spacing:.5px}
.row .pr s{color:#555;margin-right:10px}
.row .pr b{font-weight:400;color:var(--price)}
/* newsletter */
.email{left:333px;top:2961px;width:431px;height:45px;border:1px solid #ccc;font-style:italic;font-size:13px;color:#888;display:flex;align-items:center;padding-left:14px}
/* footer */
.footer{left:0;top:3077px;width:1200px;height:309px;background:var(--footer);color:#fff}
.footer h5{position:absolute;top:62px;font-family:"Open Sans",sans-serif;font-weight:400;font-size:17px;letter-spacing:.5px}
.footer ul{position:absolute;top:100px;list-style:none;font-size:13px}
.footer li{height:25.7px;display:flex;align-items:center;gap:12px}
.footer li .c{font-size:10px}
.footer .soc{width:17px;height:17px;border-radius:50%;margin-right:1px}
.footer .rule{position:absolute;left:0;top:256px;width:1200px;height:1px;background:#555}
.pay{position:absolute;top:270px;width:44px;height:26px;border-radius:2px}
</style>
</head>
<body>

<!-- top bar -->
<div class="abs topbar">
  <div class="item" style="left:80px">
    <svg width="12" height="12" viewBox="0 0 24 24"><path fill="#fff" d="M6.6 10.8a15 15 0 0 0 6.6 6.6l2.2-2.2c.3-.3.7-.4 1-.2 1.1.4 2.3.6 3.6.6.6 0 1 .4 1 1V20c0 .6-.4 1-1 1A17 17 0 0 1 3 4c0-.6.4-1 1-1h3.5c.6 0 1 .4 1 1 0 1.3.2 2.5.6 3.6.1.3 0 .7-.2 1z"/></svg>
    000 111 222 333
  </div>
  <div class="item" style="left:860px"><span style="width:18px;height:11px;background:linear-gradient(#b22 0 50%,#eee 50%);display:inline-block"></span>English ⌄</div>
  <div class="item" style="left:964px">$ USD⌄</div>
  <div class="item" style="left:1032px">
    <svg width="12" height="12" viewBox="0 0 24 24"><circle cx="12" cy="7" r="5" fill="#fff"/><path d="M2 23c0-6 4.5-9 10-9s10 3 10 9z" fill="#fff"/></svg>
    My Account
  </div>
</div>

<!-- header -->
<div class="brand" style="left:80px;top:48px">
  <span class="mark"></span><span class="name">VERDALIS</span>
  <span class="tag">HOMEOPATHIC REMEDIES</span>
</div>
<div class="abs select">All Catogories<span class="chev"></span></div>
<div class="abs search">Search entire Store here...</div>
<div class="btn" style="left:874px;top:49px;width:101px;height:29px;font-size:13px">Search</div>
<svg class="abs" style="left:1030px;top:51px" width="32" height="28" viewBox="0 0 32 28"><path d="M16 26S2 17 2 9a7 7 0 0 1 14-2 7 7 0 0 1 14 2c0 8-14 17-14 17z" fill="none" stroke="#222" stroke-width="2"/></svg>
<svg class="abs" style="left:1088px;top:50px" width="32" height="30" viewBox="0 0 32 30"><path d="M2 3h5l4 17h16l3-11H10" fill="none" stroke="#222" stroke-width="2"/><circle cx="13" cy="25" r="2" fill="#222"/><circle cx="25" cy="25" r="2" fill="#222"/><circle cx="22" cy="8" r="4" fill="#222"/></svg>

<!-- navigation -->
<nav class="abs nav">
  <a style="left:84px;width:111px;background:var(--green-light)">Home</a>
  <a style="left:195px;width:125px">About us</a><span class="sep" style="left:320px"></span>
  <a style="left:320px;width:116px">Shop</a><span class="sep" style="left:436px"></span>
  <a style="left:436px;width:101px">Offer</a><span class="sep" style="left:537px"></span>
  <a style="left:537px;width:120px">Blogs</a><span class="sep" style="left:657px"></span>
  <a style="left:657px;width:134px">Contact us</a><span class="sep" style="left:791px"></span>
  <a style="left:791px;width:184px">Deal of the Day</a><span class="sep" style="left:975px"></span>
  <a style="left:975px;width:186px">Special Discount</a>
</nav>

<!-- hero -->
<section class="abs hero" role="img" aria-label="Glass vials of white homeopathic globules with cork stoppers on a wooden table">
  <h1>The Right Remedy For You</h1>
  <p>Lorem Ipsum is simply dummy text of the printing and typesetting industry.</p>
  <div class="btn" style="left:85px;top:258px;width:173px;height:46px">Shop Now &gt;&gt;</div>
  <svg class="arrow" style="left:32px" width="24" height="26" viewBox="0 0 24 26"><path d="M20 2 6 13l14 11" fill="none" stroke="#ddd" stroke-width="5"/></svg>
  <svg class="arrow" style="left:1148px" width="24" height="26" viewBox="0 0 24 26"><path d="M4 2l14 11L4 24" fill="none" stroke="#ddd" stroke-width="5"/></svg>
  <div class="dots"><i></i><i></i><i></i><i></i></div>
</section>

<!-- features -->
<div class="feature" style="left:79px">
  <svg width="44" height="44" viewBox="0 0 44 44"><circle cx="22" cy="22" r="20" fill="none" stroke="var(--green-dark)" stroke-width="4"/><path d="M12 12c6 2 4 8 10 10s-2 10 2 14M26 6c0 6 8 4 10 10" fill="none" stroke="var(--green-dark)" stroke-width="4"/></svg>
  <div><div class="t">Free World Delivery</div><div class="s">Order Over $ 500</div></div>
</div>
<span class="fsep" style="left:318px"></span>
<div class="feature" style="left:355px">
  <svg width="44" height="44" viewBox="0 0 44 44"><circle cx="22" cy="22" r="20" fill="var(--green-dark)"/><path d="M13 22l6 6 12-12" fill="none" stroke="#fff" stroke-width="4"/></svg>
  <div><div class="t">Money Back Guarantee</div><div class="s">With a 30day</div></div>
</div>
<span class="fsep" style="left:606px"></span>
<div class="feature" style="left:645px">
  <svg width="44" height="44" viewBox="0 0 44 44"><circle cx="22" cy="22" r="20" fill="none" stroke="var(--green-dark)" stroke-width="3"/><path d="M22 10l11 6v12l-11 6-11-6V16zM11 16l11 6 11-6M22 22v12" fill="none" stroke="var(--green-dark)" stroke-width="2.5"/></svg>
  <div><div class="t">Easy &amp; Free Returns</div><div class="s">Hours: 6 Am - 10PM</div></div>
</div>
<span class="fsep" style="left:882px"></span>
<div class="feature" style="left:920px">
  <svg width="42" height="46" viewBox="0 0 42 46"><circle cx="21" cy="14" r="10" fill="var(--green-dark)"/><path d="M2 46c0-12 8-18 19-18s19 6 19 18z" fill="var(--green-dark)"/></svg>
  <div><div class="t">Best Online Support</div><div class="s">Hours: 6 Am - 10PM</div></div>
</div>

<!-- featured -->
<h2 class="sec-title" style="top:766px">Featured Products</h2>
<div class="product" style="left:80px"><div class="img"><div role="img" aria-label="Homeopathic remedy bottle with box"></div></div><div class="nm">Product Name</div><div class="pr">$00.00</div></div>
<div class="product" style="left:348px"><div class="img"><div role="img" aria-label="Mother tincture bottle with red cap"></div></div><div class="nm">Product Name</div><div class="pr">$00.00</div></div>
<div class="product" style="left:616px"><div class="img"><div role="img" aria-label="Dilution bottle with white cap"></div></div><div class="nm">Product Name</div><div class="pr">$00.00</div></div>
<div class="product" style="left:884px"><div class="img"><div role="img" aria-label="Children's tonic bottle with box"></div></div><div class="nm">Product Name</div><div class="pr">$00.00</div></div>
<div class="btn" style="left:515px;top:1235px;width:172px;height:46px">View More</div>

<!-- about -->
<div class="abs about-photo" role="img" aria-label="Homeopathic globules spilled beside yellow flowers and glass vials">
  <svg class="abs" style="left:272px;top:239px" width="74" height="74" viewBox="0 0 74 74"><circle cx="37" cy="37" r="34" fill="none" stroke="#fff" stroke-width="4"/><path d="M29 22v30l24-15z" fill="none" stroke="#fff" stroke-width="4"/></svg>
</div>
<section class="abs about">
  <h2>About us</h2>
  <p style="top:140px">Lorem Ipsum is simply dummy text of the printing and typesetting Lorem Ipsum has been the industry's standard dummy a type specimen booking text ever since the 1500s,</p>
  <p style="top:205px">when an unknown printer took a galley of type and scrambled it to make a type specimen book. It has survived not only five centuries, but also the leap into electronic typesetting, remaining essentially unchanged. It was un popularised in the 1960s</p>
  <p style="top:294px">a type specimen book is simply dummy text of the printing and typesetting Ipsum has been the industry's standard dummy a type specimen booking text ever since the 1600s,</p>
  <div class="btn" style="left:54px;top:384px;width:173px;height:46px">Read More</div>
</section>

<!-- blogs -->
<h2 class="sec-title" style="top:1938px">Blogs</h2>
<article class="blog" style="left:72px">
  <div class="img" role="img" aria-label="Shopping cart filled with remedies in front of a laptop" style="background:linear-gradient(135deg,#eef2c8,#9bc45a 50%,#c03a2a 75%,#ddd)"></div>
  <div class="meta">▦ June 24, 2019<span class="r"><span>◯ 20</span><span>♡ 12</span></span></div>
  <h3>What is Lorem Ipsum?</h3>
  <p>Lorem Ipsum is simply dummy the printing and typesetting industry. Lorem Ipsum has been the in the standard dummy.</p>
  <div class="more">Continue.. <svg width="14" height="14" viewBox="0 0 14 14"><circle cx="7" cy="7" r="6" fill="none" stroke="#444"/><path d="M6 4l3 3-3 3" fill="none" stroke="#444"/></svg></div>
</article>
<article class="blog" style="left:432px">
  <div class="img" role="img" aria-label="Hand holding a vial of amber remedy over green plants" style="background:linear-gradient(135deg,#2f4a3a,#6f8a6a 50%,#c9c4b0 80%,#e6e2d8)"></div>
  <div class="meta">▦ June 22, 2019<span class="r"><span>◯ 20</span><span>♡ 12</span></span></div>
  <h3>What is Lorem Ipsum?</h3>
  <p>Lorem Ipsum is simply dummy the printing and typesetting industry. Lorem Ipsum has been the in the standard dummy.</p>
  <div class="more">Continue.. <svg width="14" height="14" viewBox="0 0 14 14"><circle cx="7" cy="7" r="6" fill="none" stroke="#444"/><path d="M6 4l3 3-3 3" fill="none" stroke="#444"/></svg></div>
</article>
<article class="blog" style="left:793px">
  <div class="img" role="img" aria-label="Glass vials of globules with cork stoppers and green leaves" style="background:linear-gradient(135deg,#5a4a30,#8a7a5a 40%,#d8d6ce 65%,#4a6a3a)"></div>
  <div class="meta">▦ June 20, 2019<span class="r"><span>◯ 20</span><span>♡ 12</span></span></div>
  <h3>What is Lorem Ipsum?</h3>
  <p>Lorem Ipsum is simply dummy the printing and typesetting industry. Lorem Ipsum has been the in the standard dummy.</p>
  <div class="more">Continue.. <svg width="14" height="14" viewBox="0 0 14 14"><circle cx="7" cy="7" r="6" fill="none" stroke="#444"/><path d="M6 4l3 3-3 3" fill="none" stroke="#444"/></svg></div>
</article>
<div class="btn" style="left:515px;top:2424px;width:172px;height:46px;font-weight:700">View More</div>

<!-- product lists -->
<div class="list">
  <h4 style="left:81px">Best Sellers</h4>
  <h4 style="left:502px">Top Rate</h4>
  <h4 style="left:898px">On Sale</h4>
</div>
<div class="row" style="left:84px;top:2583px"><div class="th" role="img" aria-label="Remedy bottle"><i></i></div><div><div class="nm">Product Name Title</div><div class="pr"><s>$: 00.00</s><b>$: 00.00</b></div></div></div>
<div class="row" style="left:84px;top:2671px"><div class="th" role="img" aria-label="Remedy bottle"><i></i></div><div><div class="nm">Product Name Title</div><div class="pr"><s>$: 00.00</s><b>$: 00.00</b></div></div></div>
<div class="row" style="left:84px;top:2759px"><div class="th" role="img" aria-label="Remedy bottle"><i></i></div><div><div class="nm">Product Name Title</div><div class="pr"><s>$: 00.00</s><b>$: 00.00</b></div></div></div>
<div class="row" style="left:502px;top:2583px"><div class="th" role="img" aria-label="Remedy bottle with box"><i></i></div><div><div class="nm">Product Name Title</div><div class="pr"><s>$: 00.00</s><b>$: 00.00</b></div></div></div>
<div class="row" style="left:502px;top:2671px"><div class="th" role="img" aria-label="Remedy bottle with box"><i></i></div><div><div class="nm">Product Name Title</div><div class="pr"><s>$: 00.00</s><b>$: 00.00</b></div></div></div>
<div class="row" style="left:502px;top:2759px"><div class="th" role="img" aria-label="Remedy bottle with box"><i></i></div><div><div class="nm">Product Name Title</div><div class="pr"><s>$: 00.00</s><b>$: 00.00</b></div></div></div>
<div class="row" style="left:898px;top:2583px"><div class="th" role="img" aria-label="Remedy set"><i></i></div><div><div class="nm">Product Name Title</div><div class="pr"><s>$: 00.00</s><b>$: 00.00</b></div></div></div>
<div class="row" style="left:898px;top:2671px"><div class="th" role="img" aria-label="Remedy set"><i></i></div><div><div class="nm">Product Name Title</div><div class="pr"><s>$: 00.00</s><b>$: 00.00</b></div></div></div>
<div class="row" style="left:898px;top:2759px"><div class="th" role="img" aria-label="Remedy set"><i></i></div><div><div class="nm">Product Name Title</div><div class="pr"><s>$: 00.00</s><b>$: 00.00</b></div></div></div>

<!-- newsletter -->
<h2 class="sec-title" style="top:2880px;font-size:33px">Join Our Newletter</h2>
<div class="abs" style="left:0;top:2925px;width:1200px;text-align:center;font-size:13px;color:#555">Lorem Ipsum is simply dummy.</div>
<div class="abs email">Email Here</div>
<div class="btn" style="left:782px;top:2961px;width:172px;height:45px">Submit</div>

<!-- footer -->
<footer class="abs footer">
  <div class="brand" style="left:81px;top:46px;color:#fff">
    <span class="mark"></span><span class="name">VERDALIS</span>
    <span class="tag" style="color:#ccc">HOMEOPATHIC REMEDIES</span>
  </div>
  <ul style="left:84px"><li><span class="c">&gt;</span>Home</li><li><span class="c">&gt;</span>About us</li><li><span class="c">&gt;</span>Shop</li><li><span class="c">&gt;</span>Blogs</li><li><span class="c">&gt;</span>Contact us</li></ul>
  <h5 style="left:359px">Why Buy From us</h5>
  <ul style="left:359px"><li><span class="c">&gt;</span>Shipping &amp; Returns</li><li><span class="c">&gt;</span>Secure Shopping</li><li><span class="c">&gt;</span>International Shopping</li><li><span class="c">&gt;</span>Group Sales</li><li><span class="c">&gt;</span>Affiliates</li></ul>
  <h5 style="left:669px">My Account</h5>
  <ul style="left:671px"><li><span class="c">&gt;</span>Sign In</li><li><span class="c">&gt;</span>View Cart</li><li><span class="c">&gt;</span>My Product</li><li><span class="c">&gt;</span>Track My Order</li><li><span class="c">&gt;</span>Help</li></ul>
  <h5 style="left:942px;top:64px">Follow us</h5>
  <ul style="left:942px;top:102px">
    <li><span class="soc" style="background:#3b5a9a"></span>Friendbook</li>
    <li><span class="soc" style="background:#c8357a"></span>Snapgram</li>
    <li><span class="soc" style="background:#2aa3e0"></span>Chirper</li>
    <li><span class="soc" style="background:#1a78b4"></span>Linkwork</li>
    <li><span class="soc" style="background:#d8202a"></span>Viewtube</li>
  </ul>
  <div class="rule"></div>
  <div class="abs" style="left:83px;top:274px;font-size:13px;letter-spacing:.5px">Copyright©2019 Verdalis, All right reserved</div>
  <span class="pay" style="left:873px;background:#f2f2f2"></span>
  <span class="pay" style="left:923px;background:#f2f2f2"></span>
  <span class="pay" style="left:974px;background:#1d6fc2"></span>
  <span class="pay" style="left:1025px;background:#1a3f8f"></span>
  <span class="pay" style="left:1076px;background:#f2f2f2"></span>
</footer>

</body>
</html>
```